Business card revamp

we are refrigeration mechanic i need a modern professional double side business card using my current branding
The card information must have site address~ 17 Whitlow st marlow, Vic 3712 postal address~ P.o. Box 862 marlow,Vic 3713 Phone Number~0358149637 Fax Nunber~0358260518 Email address~ brucet@pelvanor.com.au Title~ Manager Licence numbers~ AU47391, NSW 681329K Web site~ www.frostrimvane.com.au

Industry/Entity Type

Business

```html
<!DOCTYPE html>
<html lang="en">
<head>
<meta charset="utf-8">
<title>Frostrim Vane – Business Card</title>
<link rel="stylesheet" href="https://fonts.googleapis.com/css2?family=Roboto:wght@300;400;700&family=Roboto+Condensed:wght@400;500;700&display=swap">
<style>
  :root {
    --backdrop-edge: #c2955a;
    --backdrop-mid: #e3c283;
    --card: #1e1916;
    --brand-grey: #c4c4c4;
    --accent-red: #b5261f;
    --accent-blue: #1a6cb8;
    --text-light: #ffffff;
    --tagline: #d8d8d8;
  }
  * { margin: 0; padding: 0; box-sizing: border-box; }
  html, body { width: 1028px; height: 1200px; overflow: hidden; }
  body {
    background: linear-gradient(180deg, var(--backdrop-edge) 0%, var(--backdrop-mid) 48%, var(--backdrop-edge) 100%);
    position: relative;
    font-family: "Roboto Condensed", "Arial Narrow", sans-serif;
  }
  .card {
    position: absolute;
    left: 48px;
    width: 927px;
    height: 529px;
    border-radius: 40px;
    background: var(--card);
  }
  .card--front { top: 46px; }
  .card--back { top: 604px; }

  .brand {
    position: absolute;
    text-align: center;
  }
  .brand__name {
    display: inline-flex;
    align-items: center;
    gap: 14px;
    font-family: "Roboto Condensed", "Arial Narrow", sans-serif;
    font-weight: 700;
    color: var(--brand-grey);
    text-transform: uppercase;
    line-height: 1;
    white-space: nowrap;
  }
  .brand__dot {
    border-radius: 50%;
    background: var(--accent-red);
    flex: none;
  }
  .brand__tagline {
    font-family: "Roboto", Arial, sans-serif;
    font-weight: 400;
    color: var(--tagline);
    text-transform: uppercase;
    white-space: nowrap;
  }

  .card--front .brand { left: 0; right: 0; top: 262px; }
  .card--front .brand__name { font-size: 66px; letter-spacing: 2px; }
  .card--front .brand__dot { width: 22px; height: 22px; }
  .card--front .brand__tagline { font-size: 16px; letter-spacing: 2.4px; margin-top: 6px; }

  .card--back .brand { left: 487px; width: 360px; top: 58px; }
  .card--back .brand__name { font-size: 37px; letter-spacing: 1px; gap: 9px; }
  .card--back .brand__dot { width: 13px; height: 13px; }
  .card--back .brand__tagline { font-size: 10.5px; letter-spacing: 1.5px; margin-top: 4px; }

  .person {
    position: absolute;
    left: 74px;
    top: 46px;
    color: var(--text-light);
    font-family: "Roboto", Arial, sans-serif;
  }
  .person__name { font-weight: 700; font-size: 26px; line-height: 32px; font-family: "Roboto Condensed", sans-serif; }
  .person__title { font-weight: 300; font-size: 27px; line-height: 34px; }

  .divider {
    position: absolute;
    left: 78px;
    right: 0;
    top: 153px;
    border-top: 2px dotted var(--accent-blue);
  }

  .contact {
    position: absolute;
    left: 484px;
    top: 198px;
    list-style: none;
    color: var(--accent-red);
    font-size: 26px;
    font-weight: 500;
  }
  .contact__item { display: flex; align-items: flex-start; gap: 16px; line-height: 36px; }
  .contact__item + .contact__item { margin-top: 18px; }
  .contact__icon { width: 26px; height: 26px; flex: none; margin-top: 5px; }

  .licences {
    position: absolute;
    left: 75px;
    top: 419px;
    color: var(--text-light);
    font-size: 24px;
    line-height: 36px;
  }
  .licences__sep { margin: 0 8px; font-weight: 300; }
</style>
</head>
<body>

  <section class="card card--front">
    <div class="brand">
      <div class="brand__name"><span class="brand__dot"></span>Frostrim Vane</div>
      <div class="brand__tagline">Heating and Cooling Specialists</div>
    </div>
  </section>

  <section class="card card--back">
    <div class="person">
      <div class="person__name">Bruce Talmage</div>
      <div class="person__title">Manager</div>
    </div>

    <div class="brand">
      <div class="brand__name"><span class="brand__dot"></span>Frostrim Vane</div>
      <div class="brand__tagline">Heating and Cooling Specialists</div>
    </div>

    <div class="divider"></div>

    <ul class="contact">
      <li class="contact__item">
        <svg class="contact__icon" viewBox="0 0 26 26" aria-hidden="true">
          <path d="M13 1C8 1 4.5 4.7 4.5 9.3 4.5 15.5 13 25 13 25s8.5-9.5 8.5-15.7C21.5 4.7 18 1 13 1z" fill="var(--accent-blue)"/>
          <circle cx="13" cy="9.5" r="3.4" fill="var(--card)"/>
        </svg>
        <span>17 Whitlow st marlow, Vic 3712<br>P.o. Box 862 marlow,Vic 3713</span>
      </li>
      <li class="contact__item">
        <svg class="contact__icon" viewBox="0 0 26 26" aria-hidden="true">
          <circle cx="13" cy="13" r="12" fill="var(--accent-blue)"/>
          <path d="M9.5 6.5l2.3 3-1.4 1.6c.8 1.9 2.2 3.4 4.2 4.4l1.5-1.4 3 2.2-1.3 2.4c-4.8.2-10.3-5.4-10.2-10.3z" fill="var(--card)"/>
        </svg>
        <span>0358149637</span>
      </li>
      <li class="contact__item">
        <svg class="contact__icon" viewBox="0 0 26 26" aria-hidden="true">
          <circle cx="13" cy="13" r="12" fill="var(--accent-blue)"/>
          <rect x="8.5" y="6.5" width="9" height="5" fill="var(--card)"/>
          <rect x="6.5" y="11.5" width="13" height="7" rx="1" fill="var(--card)"/>
          <rect x="9" y="14" width="8" height="2" fill="var(--accent-blue)"/>
        </svg>
        <span>0358260518</span>
      </li>
      <li class="contact__item">
        <svg class="contact__icon" viewBox="0 0 26 26" aria-hidden="true">
          <rect x="2" y="6" width="22" height="15" rx="1.5" fill="none" stroke="var(--accent-blue)" stroke-width="2.2"/>
          <path d="M3 7l10 8 10-8M3 20l7-6M23 20l-7-6" fill="none" stroke="var(--accent-blue)" stroke-width="2"/>
        </svg>
        <span>brucet@pelvanor.com.au</span>
      </li>
      <li class="contact__item">
        <svg class="contact__icon" viewBox="0 0 26 26" aria-hidden="true">
          <g fill="none" stroke="var(--accent-blue)" stroke-width="1.8">
            <circle cx="13" cy="13" r="11"/>
            <ellipse cx="13" cy="13" rx="5" ry="11"/>
            <path d="M2 13h22M4 7.5h18M4 18.5h18"/>
          </g>
        </svg>
        <span>www.frostrimvane.com.au</span>
      </li>
    </ul>

    <div class="licences">
      <div>Licence Numbers</div>
      <div>AU47391<span class="licences__sep">|</span>NSW 681329K</div>
    </div>
  </section>

</body>
</html>
```